Front signage

Our work consists of Industrial Electrical Automation.
We are an established company with a logo we are happy with.
Though we still need:
- a sign for our front door - 420mm x 1200mm
- a sign at the front of the building - 250mm x 1600mm

Please see attached our logo, and following our colour theme would be nice, but not essential.
Please see our website for more information on what we do
www.voltarinsystems.com.au

```html
<!DOCTYPE html>
<html lang="en">
<head>
<meta charset="utf-8">
<title>Voltarin Systems – Front Signage</title>
<link href="https://fonts.googleapis.com/css2?family=Archivo+Black&family=Roboto:wght@500&display=swap" rel="stylesheet">
<style>
  :root {
    --page-bg: #e6e6e6;
    --panel-light: #e8e8e9;
    --brand-blue: #03499a;
    --brand-orange: #fc5000;
    --brand-grey: #55565b;
    --white: #ffffff;
  }
  * { box-sizing: border-box; margin: 0; padding: 0; }
  html, body {
    width: 1200px; height: 1200px; overflow: hidden;
    background: var(--page-bg);
  }
  .sign {
    position: absolute; left: 29px; top: 511px;
    width: 1141px; height: 178px;
    display: flex;
  }
  .brand-panel {
    position: relative;
    width: 456px; height: 100%;
    background: var(--panel-light);
  }
  .brand-mark {
    position: absolute; left: 200px; top: 24px;
    width: 62px; height: 62px; border-radius: 50%;
    background: var(--brand-blue);
  }
  .brand-name {
    position: absolute; left: 0; right: 0; top: 122px;
    text-align: center;
    font-family: "Archivo Black", sans-serif;
    font-size: 21px; letter-spacing: 1.5px;
    color: var(--brand-grey);
  }
  .brand-tagline {
    position: absolute; left: 40px; right: 34px; top: 155px;
    display: flex; align-items: center; gap: 8px;
    font-family: "Roboto", sans-serif; font-weight: 500;
    font-size: 9px; letter-spacing: 1px;
    color: var(--brand-orange); white-space: nowrap;
  }
  .brand-tagline::before, .brand-tagline::after {
    content: ""; flex: 1; height: 1px; background: var(--brand-orange);
  }
  .info-panel { flex: 1; display: flex; flex-direction: column; }
  .services {
    position: relative; height: 117px;
    background: var(--brand-blue);
  }
  .service {
    position: absolute;
    display: flex; align-items: center; gap: 10px;
    font-family: "Archivo Black", sans-serif;
    font-size: 24.5px; letter-spacing: 0.6px;
    color: var(--white); line-height: 1;
  }
  .service::before {
    content: ""; width: 11px; height: 11px;
    background: var(--brand-orange);
  }
  .service--automation { left: 24px; top: 26px; }
  .service--mechanical { left: 24px; top: 70px; }
  .service--electrical { left: 433px; top: 26px; }
  .service--breakdowns { left: 433px; top: 70px; }
  .divider-line { height: 4px; background: var(--panel-light); }
  .contact {
    position: relative; flex: 1;
    background: var(--brand-orange);
    display: flex; align-items: center;
    color: var(--white);
  }
  .follow {
    margin-left: 33px;
    font-family: "Roboto", sans-serif; font-weight: 500;
    font-size: 24px;
  }
  .social-dot {
    margin-left: 10px;
    width: 27px; height: 27px; border-radius: 50%;
    background: #4a67a8;
  }
  .contact-rule {
    margin-left: 14px;
    width: 1px; height: 38px; background: var(--white);
  }
  .website {
    margin-left: 11px;
    font-family: "Archivo Black", sans-serif;
    font-size: 23.5px; letter-spacing: 0.3px;
  }
</style>
</head>
<body>
  <div class="sign">
    <section class="brand-panel">
      <div class="brand-mark"></div>
      <div class="brand-name">VOLTARIN SYSTEMS</div>
      <div class="brand-tagline">INDUSTRIAL ELECTRICAL AND MECHANICAL SERVICES</div>
    </section>
    <section class="info-panel">
      <div class="services">
        <div class="service service--automation">INDUSTRIAL AUTOMATION</div>
        <div class="service service--mechanical">MECHANICAL PROJECTS</div>
        <div class="service service--electrical">ELECTRICAL</div>
        <div class="service service--breakdowns">BREAKDOWNS</div>
      </div>
      <div class="divider-line"></div>
      <div class="contact">
        <span class="follow">Follow Us</span>
        <span class="social-dot"></span>
        <span class="contact-rule"></span>
        <span class="website">www.voltarinsystems.com.au</span>
      </div>
    </section>
  </div>
</body>
</html>
```